Residential building / Apartments for sale landing page

I need a website / landing page design for my latest development project - a residential building with 70+ apartments for sale. I need the design in layers in Photoshop/Illustrator/InDesign format with all the icons/shapes/maps/graphic assets in vector format (svg, ai, eps) as much as possible.

I prefer white website and please consider the performance/coding experience. We're not making something suitable only for a design contest with fancy parallax effects and confusing animations. We're trying to create usable and clean UI with good UX.

The website will be custom coded, i.e. I'm not using WordPress.

I know that the existing 3D photos are not good but for now you can use them or replace them with some stock photos. I'm going to create new 3D photos soon.

Industry/Entity Type

Real Estate Development

Number of Pages Required

1 page

```html
<!DOCTYPE html>
<html lang="en">
<head>
<meta charset="utf-8">
<title>Green Canopy – Apartments for Sale</title>
<link href="https://fonts.googleapis.com/css2?family=Montserrat:wght@400;600;700;800&family=Open+Sans:wght@400;600&display=swap" rel="stylesheet">
<style>
:root{
  --green:#6cb12b;
  --green-dark:#4f8e1a;
  --forest:#1d3514;
  --forest-2:#2c4d1f;
  --ink:#2b2b2b;
  --muted:#6b6b6b;
  --line:#dcdcdc;
  --paper:#ffffff;
  --mist:#f2f2f2;
}
*{box-sizing:border-box;margin:0;padding:0}
html,body{width:1200px;height:4032px;overflow:hidden}
body{position:relative;background:var(--paper);font-family:"Open Sans",Arial,sans-serif;color:var(--ink)}
.abs{position:absolute}
h1,h2,h3,.nav,.btn,.brand{font-family:"Montserrat",Arial,sans-serif}

/* hero */
.hero{left:0;top:0;width:1200px;height:660px;overflow:hidden}
.hero-photo{left:0;top:0;width:1200px;height:660px;background:linear-gradient(100deg,#2c3a2c 0%,#4a6650 30%,#7b9aa8 55%,#8fb0c0 70%,#5f7d4a 100%)}
.hero-shade{left:0;top:0;width:1200px;height:660px;background:linear-gradient(90deg,rgba(10,20,10,.55) 0%,rgba(10,20,10,.25) 45%,rgba(0,0,0,0) 70%)}
.topbar{left:0;top:0;width:1200px;height:84px}
.brand{color:#fff;font-weight:800;font-size:24px;letter-spacing:1px;display:flex;align-items:center;gap:10px}
.brand .mark{width:22px;height:22px;background:var(--green)}
.nav{left:470px;top:58px;display:flex;gap:40px;color:#fff;font-weight:600;font-size:14px;letter-spacing:.5px}
.util{top:14px;right:24px;display:flex;align-items:center;gap:18px;color:#fff;font-size:13px}
.lang{background:#fff;color:var(--ink);padding:3px 10px;border-radius:3px;font-size:12px}
.contact-btn{background:var(--green);color:#fff;font-family:"Montserrat",sans-serif;font-weight:700;font-size:12px;padding:8px 14px;border-radius:3px;display:flex;align-items:center;gap:6px}
.hero-copy{left:175px;top:222px;width:720px;display:flex;flex-direction:column;align-items:flex-start}
.hero-title{color:#fff;font-size:42px;font-weight:700;line-height:52px}
.hero-title .line{display:block;white-space:nowrap}
.hero-title .accent{color:var(--green);font-size:52px;line-height:62px}
.hero-price{margin-top:8px;color:#fff;font-family:"Montserrat",sans-serif;font-size:24px;font-weight:600;line-height:30px}
.btn{display:inline-block;background:var(--green);color:#fff;font-weight:700;font-size:14px;border-radius:24px;text-align:center}
.hero-copy .btn{margin-top:34px;width:130px;height:42px;line-height:42px}
.slider-next{left:1160px;top:310px;width:40px;height:40px;background:var(--green);display:flex;align-items:center;justify-content:center}
.dots{left:565px;top:612px;display:flex;gap:10px}
.dots span{width:9px;height:9px;border-radius:50%;background:rgba(255,255,255,.6)}
.dots span.on{background:var(--green)}

/* section headings */
.sec-head{width:1200px;text-align:center}
.sec-head .skyline{display:block;margin:0 auto 8px;width:90px;height:26px;background:linear-gradient(180deg,rgba(108,177,43,.15),rgba(108,177,43,.35))}
.sec-head h2{font-size:34px;font-weight:800;color:var(--forest);letter-spacing:1px}
.sec-head h2 em{font-style:normal;color:var(--green)}
.sec-head .rule{width:80px;height:3px;background:var(--green);margin:10px auto 0}

/* cards */
.cards{left:132px;width:936px;display:flex;box-shadow:0 6px 24px rgba(0,0,0,.12)}
.card{width:312px;background:#fff}
.card .ph{height:172px}
.card .body{height:150px;padding:22px 24px}
.card h3{font-size:18px;font-weight:700;margin-bottom:10px}
.card p{font-size:13px;line-height:1.5;color:var(--muted)}
.card.active .body{background:var(--green)}
.card.active h3,.card.active p{color:#fff}
.ph-a{background:linear-gradient(160deg,#6fa3d8,#c9d9e6 55%,#5d7d3c)}
.ph-b{background:linear-gradient(160deg,#d9e6cf,#9fc08a 60%,#5b7f3f)}
.ph-c{background:linear-gradient(160deg,#7aa8dc,#dfe8f0 55%,#7a9a66)}
.view-more{width:106px;height:30px;line-height:30px;background:#fff;color:var(--ink);font-family:"Montserrat",sans-serif;font-size:11px;font-weight:700;border-radius:16px;text-align:center;box-shadow:0 3px 10px rgba(0,0,0,.15)}

/* facilities */
.facilities{left:0;top:1220px;width:1200px;height:900px}
.facilities .bg{left:0;top:0;width:1200px;height:900px;background:linear-gradient(180deg,#223d18 0%,#2e4e22 50%,#1b3012 100%)}
.facilities .sec-head h2{color:#fff}
.facilities .lead{color:#dfe8d8;font-size:15px;margin-top:10px}
.benefit{width:420px;display:flex;gap:18px;align-items:flex-start}
.benefit .ic{width:52px;height:52px;border:2px solid var(--green);border-radius:50%;flex:none;display:flex;align-items:center;justify-content:center}
.benefit h3{color:#fff;font-size:16px;font-weight:700;margin:4px 0 4px}
.benefit p{color:#cfdac8;font-size:13px;line-height:1.5}

/* construction */
.build-photo{left:120px;top:2200px;width:400px;height:310px;background:linear-gradient(160deg,#8db4dd,#c8d6b8 50%,#4f7a35)}
.features{left:600px;top:2190px;width:480px}
.features .skyline{display:block;width:90px;height:22px;background:linear-gradient(180deg,rgba(108,177,43,.12),rgba(108,177,43,.32));margin-bottom:6px}
.features h2{font-size:30px;font-weight:800;color:var(--forest);letter-spacing:1px}
.features h2 em{font-style:normal;color:var(--green)}
.features ul{list-style:none;margin-top:22px}
.features li{font-size:13px;line-height:1.55;color:var(--muted);padding-left:22px;position:relative;margin-bottom:14px}
.features li::before{content:"";position:absolute;left:0;top:5px;width:10px;height:10px;border-radius:50%;background:var(--green)}
.features .btn{margin-top:10px;width:130px;height:40px;line-height:40px;font-size:13px}

/* gallery */
.gallery{left:0;top:2640px;width:1200px;height:480px;background:var(--mist)}
.card .caption{height:96px;padding:34px 24px;font-family:"Montserrat",sans-serif;font-size:18px;font-weight:600}
.card.active .caption{background:var(--green);color:#fff}

/* map & form */
.map{left:0;top:3150px;width:600px;height:370px;background:linear-gradient(135deg,#e6ebef,#d3dde5 60%,#c6d3dd)}
.map-pop{left:220px;top:3250px;width:180px;height:92px;background:var(--green);color:#fff;padding:14px;font-size:12px;line-height:1.4}
.map-pop strong{display:block;font-family:"Montserrat",sans-serif;font-size:13px}
.form{left:640px;top:3160px;width:440px}
.row{display:flex;gap:20px;margin-bottom:20px}
.field{flex:1;height:46px;border:1px solid var(--line);border-radius:3px;padding:14px;font-size:12px;color:#9a9a9a;background:#fff}
.field.tall{height:120px}
.form .btn{border-radius:3px;width:150px;height:42px;line-height:42px;font-size:13px;margin-top:4px}

/* footer */
.footer{left:0;top:3560px;width:1200px;height:440px;background:var(--mist)}
.f-brand{left:180px;top:3650px;color:var(--forest)}
.f-brand .brand{color:var(--forest);font-size:26px}
.f-addr{left:180px;top:3720px;font-size:13px;line-height:1.6;color:var(--muted)}
.f-phone{left:180px;top:3800px;font-size:16px;font-weight:600;color:var(--forest);display:flex;gap:8px;align-items:center}
.f-col h4{font-family:"Montserrat",sans-serif;font-size:15px;font-weight:700;color:var(--forest);margin-bottom:14px}
.f-col li{list-style:none;font-size:13px;color:var(--muted);margin-bottom:8px;padding-left:14px;position:relative}
.f-col li::before{content:"›";position:absolute;left:0;color:var(--green)}
.sub{display:flex;margin-bottom:26px}
.sub .field{flex:none;width:220px;height:40px;padding:11px 14px;border-radius:3px 0 0 3px}
.sub .btn{border-radius:0 3px 3px 0;width:110px;height:40px;line-height:40px;font-size:13px}
.social{display:flex;gap:14px}
.social span{width:36px;height:36px;border-radius:50%;background:var(--green)}
.bottom{left:0;top:4000px;width:1200px;height:32px;background:#fff;font-size:12px;color:var(--muted)}
.bottom .l{left:180px;top:9px}
.bottom .r{right:180px;top:9px}
</style>
</head>
<body>

<section class="hero abs">
  <div class="hero-photo abs" role="img" aria-label="Residential tower with planted balconies under a blue sky"></div>
  <div class="hero-shade abs"></div>
  <header class="topbar abs">
    <div class="brand abs" style="left:60px;top:26px"><span class="mark"></span>GREEN CANOPY</div>
    <nav class="nav abs"><span>GREEN CANOPY</span><span>PROJECT</span><span>APARTMENTS</span><span>LOCATION</span><span>GALLERY</span></nav>
    <div class="util abs">
      <span>(555) 210-3344</span>
      <span class="lang">English ▾</span>
      <span class="contact-btn"><svg width="12" height="12" viewBox="0 0 12 12"><path d="M2 1l2 0 1 3-1.5 1a6 6 0 003 3L8 6.5l3 1V10a1 1 0 01-1 1A9 9 0 011 2a1 1 0 011-1z" fill="#fff"/></svg>CONTACT US</span>
    </div>
  </header>
  <div class="hero-copy abs">
    <h1 class="hero-title"><span class="line">Sale of apartments directly</span><span class="line">from the investor with</span><span class="line accent">10% discount</span></h1>
    <p class="hero-price">Price from XXX EUR/m2</p>
    <a class="btn">BUY NOW</a>
  </div>
  <div class="slider-next abs"><svg width="14" height="14" viewBox="0 0 14 14"><path d="M5 2l5 5-5 5" stroke="#fff" stroke-width="2" fill="none"/></svg></div>
  <div class="dots abs"><span class="on"></span><span></span><span></span><span></span></div>
  <svg class="abs" style="left:0;top:540px" width="1200" height="120" viewBox="0 0 1200 120" preserveAspectRatio="none">
    <path d="M0 80 C300 120 500 40 800 60 C1000 74 1100 30 1200 20 L1200 120 L0 120Z" fill="#4f8e1a" opacity=".85"/>
    <path d="M0 100 C300 130 520 60 820 80 C1010 92 1110 54 1200 44 L1200 120 L0 120Z" fill="#fff"/>
  </svg>
</section>

<div class="sec-head abs" style="top:740px">
  <span class="skyline" role="img" aria-label="Small city skyline motif"></span>
  <h2>OUR <em>PROJECTS</em></h2>
  <div class="rule"></div>
</div>
<div class="cards abs" style="top:860px">
  <article class="card"><div class="ph ph-a" role="img" aria-label="Apartment building rendering"></div><div class="body"><h3>Project Name</h3><p>Lorem ipsum is simply dummy text of the printing and typesetting industry.</p></div></article>
  <article class="card active"><div class="ph ph-b" role="img" aria-label="Green residential complex rendering"></div><div class="body"><h3>Project Name</h3><p>Lorem ipsum is simply dummy text of the printing and typesetting industry.</p></div></article>
  <article class="card"><div class="ph ph-c" role="img" aria-label="Modern tower rendering"></div><div class="body"><h3>Project Name</h3><p>Lorem ipsum is simply dummy text of the printing and typesetting industry.</p></div></article>
</div>
<a class="view-more abs" style="left:547px;top:1167px">View More</a>

<section class="facilities abs">
  <div class="bg abs" role="img" aria-label="Darkened photo of a leafy apartment building"></div>
  <svg class="abs" style="left:0;top:0" width="1200" height="90" viewBox="0 0 1200 90" preserveAspectRatio="none">
    <path d="M0 0 L1200 0 L1200 30 C900 90 700 10 420 50 C240 76 100 40 0 60Z" fill="#fff"/>
  </svg>
  <div class="sec-head abs" style="top:170px">
    <h2>FACILITIES / BENEFITS</h2>
    <p class="lead">Lorem ipsum is simply dummy text of the printing and typesetting industry.</p>
  </div>
  <div class="benefit abs" style="left:120px;top:300px"><span class="ic"><svg width="24" height="24" viewBox="0 0 24 24"><path d="M12 3l6 10H6z M12 10l7 10H5z" fill="none" stroke="#6cb12b" stroke-width="2"/></svg></span><div><h3>Green areas and Gardens</h3><p>Lorem ipsum is simply dummy text of the printing and typesetting industry.</p></div></div>
  <div class="benefit abs" style="left:680px;top:300px"><span class="ic"><svg width="24" height="24" viewBox="0 0 24 24"><path d="M4 16h16M6 16V9h12v7M8 9V6h8v3" fill="none" stroke="#6cb12b" stroke-width="2"/></svg></span><div><h3>Relaxation Area</h3><p>Lorem ipsum is simply dummy text of the printing and typesetting industry.</p></div></div>
  <div class="benefit abs" style="left:120px;top:400px"><span class="ic"><svg width="24" height="24" viewBox="0 0 24 24"><rect x="4" y="4" width="16" height="16" rx="2" fill="none" stroke="#6cb12b" stroke-width="2"/><path d="M10 17V7h3a3 3 0 010 6h-3" fill="none" stroke="#6cb12b" stroke-width="2"/></svg></span><div><h3>Parking Spaces</h3><p>Lorem ipsum is simply dummy text of the printing and typesetting industry.</p></div></div>
  <div class="benefit abs" style="left:680px;top:400px"><span class="ic"><svg width="24" height="24" viewBox="0 0 24 24"><circle cx="12" cy="7" r="3" fill="none" stroke="#6cb12b" stroke-width="2"/><path d="M6 20l3-8h6l3 8" fill="none" stroke="#6cb12b" stroke-width="2"/></svg></span><div><h3>Childrens Playground</h3><p>Lorem ipsum is simply dummy text of the printing and typesetting industry.</p></div></div>
  <div class="benefit abs" style="left:120px;top:500px"><span class="ic"><svg width="24" height="24" viewBox="0 0 24 24"><circle cx="6" cy="16" r="4" fill="none" stroke="#6cb12b" stroke-width="2"/><circle cx="18" cy="16" r="4" fill="none" stroke="#6cb12b" stroke-width="2"/><path d="M6 16l5-8h5l2 8" fill="none" stroke="#6cb12b" stroke-width="2"/></svg></span><div><h3>Bicycle Parking</h3><p>Lorem ipsum is simply dummy text of the printing and typesetting industry.</p></div></div>
  <div class="benefit abs" style="left:680px;top:500px"><span class="ic"><svg width="24" height="24" viewBox="0 0 24 24"><path d="M3 16c3-2 6 2 9 0s6 2 9 0M3 20c3-2 6 2 9 0s6 2 9 0M8 13V4M16 13V4" fill="none" stroke="#6cb12b" stroke-width="2"/></svg></span><div><h3>Pool</h3><p>Lorem ipsum is simply dummy text of the printing and typesetting industry.</p></div></div>
  <div class="benefit abs" style="left:120px;top:600px"><span class="ic"><svg width="24" height="24" viewBox="0 0 24 24"><path d="M3 12h18M6 8v8M18 8v8M3 10v4M21 10v4" fill="none" stroke="#6cb12b" stroke-width="2"/></svg></span><div><h3>Outside Workout Area</h3><p>Lorem ipsum is simply dummy text of the printing and typesetting industry.</p></div></div>
  <div class="benefit abs" style="left:680px;top:600px"><span class="ic"><svg width="24" height="24" viewBox="0 0 24 24"><path d="M7 3v18M5 3v5a2 2 0 004 0V3M17 21V3c-3 2-3 8 0 9" fill="none" stroke="#6cb12b" stroke-width="2"/></svg></span><div><h3>Restaurant</h3><p>Lorem ipsum is simply dummy text of the printing and typesetting industry.</p></div></div>
  <div class="benefit abs" style="left:120px;top:700px"><span class="ic"><svg width="24" height="24" viewBox="0 0 24 24"><rect x="5" y="11" width="14" height="10" rx="2" fill="none" stroke="#6cb12b" stroke-width="2"/><path d="M8 11V7a4 4 0 018 0v4" fill="none" stroke="#6cb12b" stroke-width="2"/></svg></span><div><h3>NFC Controlled Access</h3><p>Lorem ipsum is simply dummy text of the printing and typesetting industry.</p></div></div>
  <div class="benefit abs" style="left:680px;top:700px"><span class="ic"><svg width="24" height="24" viewBox="0 0 24 24"><circle cx="6" cy="12" r="2" fill="#6cb12b"/><circle cx="12" cy="12" r="2" fill="#6cb12b"/><circle cx="18" cy="12" r="2" fill="#6cb12b"/></svg></span><div><h3>ETC</h3><p>Lorem ipsum is simply dummy text of the printing and typesetting industry.</p></div></div>
  <svg class="abs" style="left:0;top:820px" width="1200" height="80" viewBox="0 0 1200 80" preserveAspectRatio="none">
    <path d="M0 50 C300 10 600 70 900 40 C1050 26 1130 40 1200 30 L1200 80 L0 80Z" fill="#fff"/>
  </svg>
</section>

<div class="build-photo abs" role="img" aria-label="Apartment tower with terraces full of plants"></div>
<div class="features abs">
  <span class="skyline" role="img" aria-label="Small city skyline motif"></span>
  <h2>CONSTRUCTION <em>FEATURES</em></h2>
  <ul>
    <li>Alu windows – triple glazing with high temperature and noise insulation efficiency.</li>
    <li>Soundproofing – acoustic membranes between floors with dense cement walls 25 cm thick.</li>
    <li>High ceilings – 2.7 m high ceilings giving the light and space you need.</li>
    <li>Thermal insulation system – mineral wool facade 15 cm thick on all outer walls.</li>
  </ul>
  <a class="btn">LEARN MORE</a>
</div>

<section class="gallery abs">
  <svg class="abs" style="left:0;top:0" width="1200" height="50" viewBox="0 0 1200 50" preserveAspectRatio="none">
    <path d="M0 0 L1200 0 L1200 20 C900 50 500 0 0 30Z" fill="#fff"/>
  </svg>
  <div class="sec-head abs" style="top:60px">
    <span class="skyline" role="img" aria-label="Small city skyline motif"></span>
    <h2>OUR <em>GALLERY</em></h2>
    <div class="rule"></div>
  </div>
  <div class="cards abs" style="top:180px">
    <article class="card"><div class="ph ph-a" role="img" aria-label="Construction progress photo, April"></div><div class="caption">April 2021</div></article>
    <article class="card active"><div class="ph ph-b" role="img" aria-label="Construction progress photo, March"></div><div class="caption">March 2021</div></article>
    <article class="card"><div class="ph ph-c" role="img" aria-label="Construction progress photo, February"></div><div class="caption">February 2021</div></article>
  </div>
  <a class="view-more abs" style="left:547px;top:433px">View More</a>
</section>

<div class="map abs" role="img" aria-label="Street map showing the building location"></div>
<div class="map-pop abs"><strong>Green Canopy</strong>Lorem ipsum is simply text of the printing.</div>
<svg class="abs" style="left:290px;top:3346px" width="20" height="28" viewBox="0 0 20 28"><path d="M10 27C4 18 1 14 1 10a9 9 0 0118 0c0 4-3 8-9 17z" fill="#6cb12b"/><circle cx="10" cy="10" r="3.5" fill="#fff"/></svg>
<form class="form abs">
  <div class="row"><div class="field">First name</div><div class="field">Last Name</div></div>
  <div class="row"><div class="field">Email Address</div></div>
  <div class="row"><div class="field tall">Message</div></div>
  <a class="btn">Send Message</a>
</form>

<footer class="footer abs">
  <svg class="abs" style="left:0;top:0" width="1200" height="50" viewBox="0 0 1200 50" preserveAspectRatio="none">
    <path d="M0 0 L1200 0 L1200 10 C800 50 400 10 0 36Z" fill="#fff"/>
  </svg>
</footer>
<div class="f-brand abs"><div class="brand"><span class="mark"></span>GREEN CANOPY</div></div>
<p class="f-addr abs">Green Canopy<br>1800 Orchard Lane<br>Fairview, 40210</p>
<div class="f-phone abs"><svg width="16" height="16" viewBox="0 0 12 12"><path d="M2 1l2 0 1 3-1.5 1a6 6 0 003 3L8 6.5l3 1V10a1 1 0 01-1 1A9 9 0 011 2a1 1 0 011-1z" fill="#6cb12b"/></svg>(555) 210-3344</div>
<div class="f-col abs" style="left:520px;top:3640px">
  <h4>COMPANY</h4>
  <ul><li>Green Canopy</li><li>Project</li><li>Apartments</li><li>Location</li><li>Gallery</li><li>Contact Us</li></ul>
</div>
<div class="f-col abs" style="left:700px;top:3640px">
  <h4>SUBSCRIBE</h4>
  <div class="sub"><div class="field">Email address</div><a class="btn">Subscribe</a></div>
  <h4>FOLLOW US</h4>
  <div class="social"><span></span><span></span><span></span></div>
</div>
<div class="bottom abs">
  <span class="l abs">© 2022 Green Canopy. All Rights Reserved.</span>
  <span class="r abs">Privacy Policy | Terms of Use</span>
</div>

</body>
</html>
```